DALMO-FIX
Business Card, Stationary, Envelope & Invoice Design
Hi Designers, just uploaded a png file, colors in blue, can we try that???
Thanks
Hi Designers, We would like to have a folder desing also.

```html
<!DOCTYPE html>
<html lang="en">
<head>
<meta charset="utf-8">
<title>DALMO-FIX Business Card Options</title>
<link href="https://fonts.googleapis.com/css2?family=Michroma&family=Open+Sans:ital,wght@0,400;0,700;1,400&display=swap" rel="stylesheet">
<style>
  :root {
    --board: #3b3b3d;
    --orange: #f39a1e;
    --orange-deep: #b8600a;
    --brown: #3a2108;
    --black: #0d0d0d;
    --white: #ffffff;
    --ink: #2a2a2a;
    --ink-soft: #555555;
    --label: #e8e8e8;
  }
  * { margin: 0; padding: 0; box-sizing: border-box; }
  html, body { width: 1200px; height: 809px; overflow: hidden; }
  body {
    background: radial-gradient(ellipse at center, #4a4a4c 0%, var(--board) 60%, #2c2c2e 100%);
    font-family: "Open Sans", sans-serif;
    position: relative;
  }
  .card {
    position: absolute;
    width: 535px;
    height: 318px;
    border-radius: 14px;
    overflow: hidden;
    box-shadow: 0 4px 10px rgba(0,0,0,0.45);
  }
  .card--front-a { left: 60px; top: 53px;
    background: radial-gradient(ellipse at 45% 45%, #f6a327 0%, #d97d12 40%, #7a420a 80%, var(--brown) 100%); }
  .card--front-b { left: 636px; top: 53px; background: var(--black); }
  .card--back-a { left: 60px; top: 456px; background: var(--white); }
  .card--back-b { left: 636px; top: 456px; background: var(--white); }

  .card--front-b::after {
    content: ""; position: absolute; left: 0; right: 0; bottom: 22px; height: 2px;
    background: linear-gradient(90deg, transparent, var(--orange), transparent);
  }
  .card--back-a .base-band {
    position: absolute; left: 0; right: 0; bottom: 0; height: 26px;
    background: linear-gradient(180deg, #fff 0%, #f7c77d 40%, var(--orange) 70%, var(--orange-deep) 100%);
  }

  .brand {
    position: absolute;
    display: flex; align-items: center; gap: 8px;
    font-family: "Open Sans", sans-serif;
    font-weight: 700;
    font-size: 34px;
    letter-spacing: 1px;
    white-space: nowrap;
  }
  .brand__mark { width: 16px; height: 16px; background: var(--orange); }
  .card--front-a .brand { left: 38px; top: 148px; color: var(--white); }
  .card--front-a .brand__mark { background: var(--white); }
  .card--front-b .brand { left: 38px; top: 148px; color: var(--white); }
  .card--back-a .brand { left: 24px; top: 160px; color: var(--ink); font-size: 26px; gap: 7px; }
  .card--back-a .brand__mark { width: 13px; height: 13px; }
  .tagline {
    position: absolute; font-size: 9px; font-style: italic; white-space: nowrap;
  }
  .card--front-a .tagline, .card--front-b .tagline { left: 120px; top: 196px; color: #f1e3cf; }
  .card--back-a .tagline { left: 66px; top: 198px; color: var(--ink-soft); font-size: 8px; }

  .contact {
    position: absolute; left: 312px; top: 30px;
    font-size: 11px; line-height: 16px; font-style: italic;
    white-space: nowrap;
  }
  .card--back-a .contact { left: 290px; top: 22px; }
  .contact__name { font-size: 13px; font-style: normal; }
  .contact__role { font-style: normal; margin-bottom: 10px; }
  .contact__row { display: flex; align-items: center; gap: 6px; }
  .contact__row.indent { padding-left: 16px; }
  .contact__group { margin-bottom: 8px; }
  .icon { width: 10px; height: 10px; flex: none; }
  .card--front-a .contact { color: var(--white); }
  .card--front-a .icon { fill: var(--white); }
  .card--front-b .contact { color: #dddddd; }
  .card--front-b .contact__name { color: var(--orange); }
  .card--front-b .icon { fill: var(--orange); }
  .card--back-a .contact { color: var(--ink); }
  .card--back-a .contact__name { color: var(--orange-deep); }
  .card--back-a .icon { fill: var(--orange); }

  .emblem {
    position: absolute; left: 235px; top: 118px; width: 64px; height: 64px; background: var(--orange);
  }
  .web-line {
    position: absolute; left: 0; right: 0; bottom: 24px; text-align: center;
    font-size: 14px; font-style: italic; color: var(--ink);
  }

  .label {
    position: absolute; width: 535px; text-align: center;
    font-family: "Michroma", sans-serif; font-size: 15px; letter-spacing: 2px;
    color: var(--label); white-space: nowrap;
  }
</style>
</head>
<body>
  <svg width="0" height="0" style="position:absolute">
    <defs>
      <symbol id="i-pin" viewBox="0 0 10 10"><path d="M5 0a3.5 3.5 0 0 0-3.5 3.5C1.5 6 5 10 5 10s3.5-4 3.5-6.5A3.5 3.5 0 0 0 5 0zm0 5a1.4 1.4 0 1 1 0-2.8A1.4 1.4 0 0 1 5 5z"/></symbol>
      <symbol id="i-phone" viewBox="0 0 10 10"><path d="M2 0.5l2 2-1 1.2c.6 1.3 1.6 2.3 2.8 2.8l1.2-1 2 2-1.3 1.7C4.5 9 1 5.5.3 1.8z"/></symbol>
      <symbol id="i-mobile" viewBox="0 0 10 10"><rect x="2.5" y="0" width="5" height="10" rx="1"/></symbol>
      <symbol id="i-fax" viewBox="0 0 10 10"><rect x="0" y="3" width="10" height="5" rx="1"/><rect x="2" y="0" width="6" height="3"/></symbol>
      <symbol id="i-mail" viewBox="0 0 10 10"><rect x="0" y="2" width="10" height="6" rx="1"/></symbol>
      <symbol id="i-web" viewBox="0 0 10 10"><circle cx="5" cy="5" r="5"/></symbol>
    </defs>
  </svg>

  <section class="card card--front-a">
    <div class="brand"><span class="brand__mark"></span>DALMO-FIX</div>
    <div class="tagline">IT &amp; Automation Consulting Services</div>
    <div class="contact">
      <div class="contact__name">Luis Ortega</div>
      <div class="contact__role">Managing Director</div>
      <div class="contact__group">
        <div class="contact__row"><svg class="icon"><use href="#i-pin"/></svg>Calle Robles 214</div>
        <div class="contact__row indent">Col. Jardines</div>
        <div class="contact__row indent">C.P. 44100 Ciudad Nueva</div>
      </div>
      <div class="contact__group">
        <div class="contact__row"><svg class="icon"><use href="#i-phone"/></svg>+(52) 555 0142300</div>
        <div class="contact__row"><svg class="icon"><use href="#i-mobile"/></svg>+(52) 555 0187211</div>
        <div class="contact__row"><svg class="icon"><use href="#i-fax"/></svg>+(52) 555 0142301</div>
      </div>
      <div class="contact__row"><svg class="icon"><use href="#i-mail"/></svg>luis.ortega@dalmo-fix.com</div>
      <div class="contact__row"><svg class="icon"><use href="#i-web"/></svg>www.Dalmo-Fix.com</div>
    </div>
  </section>
  <div class="label" style="left:60px; top:404px;">Business Card Front Option A</div>

  <section class="card card--front-b">
    <div class="brand"><span class="brand__mark"></span>DALMO-FIX</div>
    <div class="tagline">IT &amp; Automation Consulting Services</div>
    <div class="contact">
      <div class="contact__name">Luis Ortega</div>
      <div class="contact__role">Managing Director</div>
      <div class="contact__group">
        <div class="contact__row"><svg class="icon"><use href="#i-pin"/></svg>Calle Robles 214</div>
        <div class="contact__row indent">Col. Jardines</div>
        <div class="contact__row indent">C.P. 44100 Ciudad Nueva</div>
      </div>
      <div class="contact__group">
        <div class="contact__row"><svg class="icon"><use href="#i-phone"/></svg>+(52) 555 0142300</div>
        <div class="contact__row"><svg class="icon"><use href="#i-mobile"/></svg>+(52) 555 0187211</div>
        <div class="contact__row"><svg class="icon"><use href="#i-fax"/></svg>+(52) 555 0142301</div>
      </div>
      <div class="contact__row"><svg class="icon"><use href="#i-mail"/></svg>luis.ortega@dalmo-fix.com</div>
      <div class="contact__row"><svg class="icon"><use href="#i-web"/></svg>www.Dalmo-Fix.com</div>
    </div>
  </section>
  <div class="label" style="left:636px; top:404px;">Business Card Front Option B</div>

  <section class="card card--back-a">
    <div class="brand"><span class="brand__mark"></span>DALMO-FIX</div>
    <div class="tagline">IT &amp; Automation Consulting Services</div>
    <div class="contact">
      <div class="contact__name">Luis Ortega</div>
      <div class="contact__role">Managing Director</div>
      <div class="contact__group">
        <div class="contact__row"><svg class="icon"><use href="#i-pin"/></svg>Calle Robles 214</div>
        <div class="contact__row indent">Col. Jardines</div>
        <div class="contact__row indent">C.P. 44100 Ciudad Nueva</div>
      </div>
      <div class="contact__group">
        <div class="contact__row"><svg class="icon"><use href="#i-phone"/></svg>+(52) 555 0142300</div>
        <div class="contact__row"><svg class="icon"><use href="#i-mobile"/></svg>+(52) 555 0187211</div>
        <div class="contact__row"><svg class="icon"><use href="#i-fax"/></svg>+(52) 555 0142301</div>
      </div>
      <div class="contact__row"><svg class="icon"><use href="#i-mail"/></svg>luis.ortega@dalmo-fix.com</div>
      <div class="contact__row"><svg class="icon"><use href="#i-web"/></svg>www.Dalmo-Fix.com</div>
    </div>
    <div class="base-band"></div>
  </section>
  <div class="label" style="left:60px; top:784px;">Business Card Back Option A</div>

  <section class="card card--back-b">
    <div class="emblem"></div>
    <div class="web-line">www.Dalmo-Fix.com</div>
  </section>
  <div class="label" style="left:636px; top:784px;">Business Card Back Option B</div>
</body>
</html>
```